Natural Essential Oil Packaging

We would like you to develop a line of packaging for natural essential oil products from a company named “Kieu Phong Dat.”
List of items to be designed:
- 01 Company logo
- Air freshener (spray) product: 01 Package design + 01 label design
- 02 essential oil (glass containers) variants: 02 Label designs + 01 “how to use” attached instruction tag
Description:
A. Company logo:
- Company name: Kieu Phong Dat (“Tram” is the Vietnamese name for melaleuca);
- symbolizing "pure, natural, untouched, Kieu Phong Dat, essential,";
- should consist of text and graphic;
- should suggest a stylized drop of oil;
B. Air freshener (spray) product (Packaging and label design)
a. Product description
- Oil extracted from the unique Vietnamese cajeput trees
- Strength: pleasant aroma, air cleansing, virus and bacteria cleaning and prevention, insect expelling
- Used for: air refreshing, relaxing, spa-effect, air cleaning, air-born virus prevention (flu virus), insect expelling
- Application: air spray
b. Package to design: 170ml glass spray bottle
c. Label text for design: brand name: Zovetta + variant name “Lemongrass” + Air Freshener + Melaleuca Essential Oil
C. 02 essential oil (glass containers) variants (Label and Instrution Tag designs)
a. Production description:
i. 02 product variant under the brand name Quirandol
1 - Vietnamese Cajeput Oil: Special breed of cajeput only found in Vietnam, known for amazingly pleasant fragrance giving senses of relaxation, refreshment, peace while at the same time, driving off potential disease carrying elements in the air
2 - Australian tea trea oil: Australian breed of malaleuca known for effective healing of skin from various types of infection, skin protection and highly effective oral hygiene
ii. Product values:
1. 100% pure oil, 100% organic, 100% environment and human friendly, NO chemical
2. aiming to promote human’s well being, health, nature sustainability, improve living environment
3. both products are about nurturing, uplifting, healing and recovering
4. both place their values on authenticity, originality, nature, exotic natural ingredients, green and organic life style
5. both have zero chemical and artificial substance hence 100% safe for long time and frequent usage
iii. SKU: 10ml glass container
iv. Application: for both topical and oral use
b. Label text for design:
i. brand name: Quirandol + variant name: Cajeput Oil / Tea Tree Oil
D. Creative elements are suggested to be communicating organicity, understated premiumness, nature, lightness, nurturing
PLEASE SEE ATTACHED FILES FOR BETTER BRIEF DETAILS AND LAYOUTS.

```html
<!DOCTYPE html>
<html lang="en">
<head>
<meta charset="utf-8">
<title>Quirandol Vietnamese Tea Tree Oil – Instruction Tag</title>
<link rel="stylesheet" href="https://fonts.googleapis.com/css2?family=Montserrat:ital,wght@0,400;0,700;1,400;1,700&family=Didact+Gothic&display=swap">
<style>
  :root {
    --leaf-green: #45865a;
    --leaf-light: #f3f5ef;
    --brand-purple: #5e2f78;
    --copy-purple: #4b2a63;
    --lime: #d3dc27;
    --teal: #1a9c9a;
    --ink: #111111;
    --white: #ffffff;
  }
  html, body {
    margin: 0;
    padding: 0;
    width: 1200px;
    height: 978px;
    overflow: hidden;
    background: var(--white);
  }
  .tag {
    position: relative;
    width: 1200px;
    height: 978px;
    font-family: "Montserrat", sans-serif;
  }
  .leaves {
    position: absolute;
    inset: 0;
  }
  .block { position: absolute; margin: 0; }

  .mini-brand {
    font-family: "Montserrat", sans-serif;
    font-weight: 700;
    color: var(--brand-purple);
    text-align: center;
    line-height: 1;
  }
  .mini-sub {
    font-family: "Montserrat", sans-serif;
    font-weight: 700;
    color: var(--lime);
    text-align: center;
    line-height: 1;
    text-shadow: 1px 1px 1px rgba(0,0,0,.35);
  }

  .top-brand { left: 200px; top: 18px; width: 280px; font-size: 38px; }
  .top-sub { left: 190px; top: 66px; width: 300px; font-size: 19px; }

  .story {
    left: 28px; top: 103px; width: 532px;
    font-family: "Didact Gothic", sans-serif;
    font-style: italic;
    font-size: 19.5px;
    line-height: 24px;
    color: var(--copy-purple);
    text-align: justify;
    text-align-last: center;
  }
  .section-title {
    font-family: "Montserrat", sans-serif;
    font-weight: 700;
    color: var(--white);
    font-size: 17px;
    text-align: center;
  }
  .directions-title { left: 680px; top: 52px; width: 300px; }
  .directions-copy, .ingredients-copy {
    font-weight: 700;
    font-style: italic;
    color: var(--ink);
    text-align: justify;
    text-align-last: center;
  }
  .directions-copy {
    left: 603px; top: 88px; width: 454px;
    font-size: 16px; line-height: 23.5px;
  }

  .hero-brand {
    left: 0; top: 285px; width: 1200px;
    display: flex; align-items: center; justify-content: center; gap: 30px;
    font-weight: 700;
    font-size: 200px;
    line-height: 1;
    color: var(--brand-purple);
  }
  .hero-dot {
    width: 120px; height: 120px; border-radius: 50%;
    background: var(--brand-purple);
    flex: none;
  }
  .hero-sub {
    left: 0; top: 535px; width: 1200px;
    font-weight: 700;
    font-size: 84px;
    line-height: 1;
    letter-spacing: 1px;
    color: var(--lime);
    text-align: center;
    text-shadow: 2px 3px 3px rgba(0,0,0,.35);
  }

  .ingredients-title { left: 172px; top: 781px; width: 300px; }
  .ingredients-copy {
    left: 92px; top: 815px; width: 462px;
    font-size: 15px; line-height: 19.5px;
  }

  .maker {
    left: 786px; top: 752px; width: 210px; height: 68px;
    display: flex; align-items: center; gap: 10px;
  }
  .maker-dot {
    width: 40px; height: 40px; border-radius: 50%;
    background: var(--teal); flex: none;
  }
  .maker-name {
    font-family: "Didact Gothic", sans-serif;
    font-size: 24px; line-height: 1.05;
    color: var(--teal);
  }

  .bottom-brand { left: 605px; top: 850px; width: 400px; font-size: 62px; }
  .bottom-sub { left: 605px; top: 921px; width: 400px; font-size: 27px; }
</style>
</head>
<body>
<main class="tag">
  <svg class="leaves" width="1200" height="978" viewBox="0 0 1200 978" aria-hidden="true">
    <defs>
      <linearGradient id="leafTone" x1="0" y1="0" x2="1" y2="0">
        <stop offset="0" stop-color="var(--leaf-green)"/>
        <stop offset="0.18" stop-color="#5f9872"/>
        <stop offset="0.46" stop-color="var(--leaf-light)"/>
        <stop offset="0.8" stop-color="#4d8c62"/>
        <stop offset="1" stop-color="var(--leaf-green)"/>
      </linearGradient>
    </defs>
    <path class="leaf-top" d="M-10,130 Q600,-120 1165,130 Q600,380 -10,130 Z" fill="url(#leafTone)"/>
    <circle cx="537" cy="39" r="20" fill="var(--white)"/>
    <circle cx="622" cy="39" r="20" fill="var(--white)"/>
    <path class="leaf-bottom" d="M-10,845 Q600,595 1165,845 Q600,1095 -10,845 Z" fill="url(#leafTone)"/>
    <circle cx="537" cy="756" r="20" fill="var(--white)"/>
    <circle cx="622" cy="756" r="20" fill="var(--white)"/>
  </svg>

  <p class="block mini-brand top-brand">Quirandol</p>
  <p class="block mini-sub top-sub">Vietnamese Tea Tree Oil</p>
  <p class="block story">This special breed of cajeput is found only in Vietnam. It is known for its amazingly pleasant fragrance that offers a sense of relaxation, refreshment and peace while at the same time, driving off potential disease carrying elements in the air.</p>

  <h2 class="block section-title directions-title">Directions for Use:</h2>
  <p class="block directions-copy">Place three drops of Quirandol Vietnamese Cajeput Oil into your favorite diffuser or into a wide bowl of boiling hot water. Breathe slowly and deeply.</p>

  <h1 class="block hero-brand"><span class="hero-dot"></span>Quirandol</h1>
  <p class="block hero-sub">Vietnamese Tea Tree Oil</p>

  <h2 class="block section-title ingredients-title">INGREDIENTS</h2>
  <p class="block ingredients-copy">Water, alcohol, melaleuca (tea) tree oil, Water, alcohol, melaleuca (tea) tree oil Water, alcohol, melaleuca (tea) tree oil</p>

  <div class="block maker">
    <span class="maker-dot"></span>
    <span class="maker-name">Kieu Phong Dat</span>
  </div>

  <p class="block mini-brand bottom-brand">Quirandol</p>
  <p class="block mini-sub bottom-sub">Vietnamese Tea Tree Oil</p>
</main>
</body>
</html>
```